Steady Harbour Coaching Business Card

We need a business card for a new business based in Sydney Australia called "Steady Harbour Coaching". The business provides the following:
1. Resilience systems for individuals - Developing personalised resilience programs that increase stress tolerance, improve work effectiveness and minimise stress responses to challenge.
2. Group Resilience Training for Leaders and managers - Delivering Resilience training packages and ongoing support to leadership cadres within organisations.
3. High Risk Resilience Training - providing resilience training for High Risk professions such as emergency responders, military and police.

Target Market(s)

Corporate / Military / Emergency Responders

Industry/Entity Type

Leadership

Contact Information for Business Card

Steady Harbour Coaching, Derek Falwood, 7/19 Kestrel St Penbrook 2093, quiet.morning.tide@mailpost.example, www.steadyharbourcoaching.example.au, M# 0417603842
Personalised Mental Resilience Systems for leaders and high risk professions

Requirements
Must have
• 1. Creation of a logo/graphic - to include 3 elements:
a. Military
b.Corporate
c. Emergency Responder.

As long as those 3 elements are included - I am open to any potential designs. Preference given to those who can create a logo out of the above three elements.

```html
<!DOCTYPE html>
<html lang="en">
<head>
<meta charset="utf-8">
<title>Steady Harbour Coaching – Business Card</title>
<link href="https://fonts.googleapis.com/css2?family=Open+Sans:wght@400;600&display=swap" rel="stylesheet">
<style>
  :root {
    --page: #ececec;
    --card: #ffffff;
    --red: #ea2a41;
    --blue: #3a66b5;
    --black: #231f20;
    --ink: #1f1f1f;
    --green: #8cc63f;
  }
  * { margin: 0; padding: 0; box-sizing: border-box; }
  html, body {
    width: 1200px; height: 800px; overflow: hidden;
    background: var(--page);
    font-family: "Open Sans", Arial, sans-serif;
  }
  .card {
    position: absolute; left: 150px; top: 140px;
    width: 900px; height: 520px;
    background: var(--card);
    box-shadow: 0 10px 30px rgba(0,0,0,.18);
    overflow: hidden;
  }
  .card-bands { position: absolute; inset: 0; width: 900px; height: 520px; }
  .brand {
    position: absolute; left: 70px; top: 92px;
    display: flex; align-items: center; gap: 18px;
  }
  .brand-square {
    width: 58px; height: 58px; border-radius: 10px; background: var(--green);
  }
  .brand-name {
    font-size: 36px; font-weight: 400; color: var(--ink); letter-spacing: .2px;
  }
  .contact {
    position: absolute; left: 92px; top: 250px;
  }
  .contact-name {
    color: var(--red); font-size: 24px; font-weight: 600; margin-bottom: 10px;
  }
  .contact-list { list-style: none; }
  .contact-item {
    display: flex; align-items: center; gap: 12px;
    font-size: 20px; line-height: 31px; color: var(--ink);
  }
  .contact-icon { width: 20px; height: 20px; flex: none; }
  .tagline {
    position: absolute; left: 0; right: 0; bottom: 0; height: 50px;
    display: flex; align-items: center; justify-content: center;
    color: #fff; font-size: 17px; letter-spacing: .6px; text-transform: uppercase;
  }
</style>
</head>
<body>
  <div class="card">
    <svg class="card-bands" viewBox="0 0 900 520" aria-hidden="true">
      <path d="M680 0 H900 V446 H0 V420 Z" fill="var(--red)"/>
      <path d="M0 0 H690 L858 372 Q876 418 826 420 H0 Z" fill="var(--card)"/>
      <rect x="0" y="446" width="900" height="7" fill="var(--card)"/>
      <rect x="0" y="453" width="900" height="17" fill="var(--blue)"/>
      <rect x="0" y="470" width="900" height="50" fill="var(--black)"/>
    </svg>

    <div class="brand">
      <span class="brand-square"></span>
      <span class="brand-name">Steady Harbour Coaching</span>
    </div>

    <div class="contact">
      <p class="contact-name">Derek Falwood</p>
      <ul class="contact-list">
        <li class="contact-item">
          <svg class="contact-icon" viewBox="0 0 20 20"><rect x="5" y="1" width="10" height="18" rx="2" fill="var(--red)"/><rect x="7" y="4" width="6" height="9" fill="#fff"/></svg>
          0417603842
        </li>
        <li class="contact-item">
          <svg class="contact-icon" viewBox="0 0 20 20"><path d="M10 2 L19 10 H16 V18 H12 V13 H8 V18 H4 V10 H1 Z" fill="var(--red)"/></svg>
          7/19 Kestrel St Penbrook 2093
        </li>
        <li class="contact-item">
          <svg class="contact-icon" viewBox="0 0 20 20"><rect x="1" y="4" width="18" height="13" rx="2" fill="var(--red)"/><path d="M2 5 L10 11 L18 5" stroke="#fff" stroke-width="1.8" fill="none"/></svg>
          quiet.morning.tide@mailpost.example
        </li>
        <li class="contact-item">
          <svg class="contact-icon" viewBox="0 0 20 20"><circle cx="10" cy="10" r="8.5" fill="var(--red)"/><g stroke="#fff" stroke-width="1.3" fill="none"><ellipse cx="10" cy="10" rx="3.5" ry="8.5"/><path d="M1.5 10 H18.5 M3 6 H17 M3 14 H17"/></g></svg>
          www.steadyharbourcoaching.example.au
        </li>
      </ul>
    </div>

    <p class="tagline">Personalised mental resilience systems for leaders and high risk professions</p>
  </div>
</body>
</html>
```